New Business Card Design Project

I need a design for business cards, i am an electrical business called "Tandor Electrical and Communications" i need the cards to be double sided with the company logo on the back (attached) the front needs to say my company name, web site, email address, telephone number, and ABN number and electrical license number. I am open to different arrangements of the information but would like the background to be incorporating something electrical or something that looks smart. open to all additional ideas also.

The company colours are orange and grey see logo attached.

Business Name: Tandor Electrical and Communications
Website: tandorelectricalandcomms.example.au
Email: brent@tandorelectricalandcomms.example.au
Telephone(mobile): 0481203967
ABN: 71829034618
Lic No: 830472F

Target Market(s)

Business entities, Project Managers, Accounts, Clients

Industry/Entity Type

Electrician

Contact Information for Business Card

I need a design for business cards, i am an electrical business called "Tandor Electrical and Communications" i need the cards to be double sided with the company logo on the back (attached) the front needs to say my company name

Font styles to use
Serif
Sans Serif

Colors
f37122
5c5c5c

Requirements
Must have
• Must have the Logo on the back open to different ways of it being on the back but had in mind to keep it central but again open to other options
Nice to have
• A real modern cool background that is eye catching yet contemporary
Should not have
• No backgrounds of a light bulb or plug or anything like that

```html
<!DOCTYPE html>
<html lang="en">
<head>
<meta charset="utf-8">
<title>Tandor Electrical and Communications – Business Cards</title>
<link href="https://fonts.googleapis.com/css2?family=Source+Sans+3:wght@400;600&display=swap" rel="stylesheet">
<style>
  :root {
    --stage-top: #2a2a2a;
    --stage-bottom: #050505;
    --card-white: #ffffff;
    --brand-orange: #f4a21c;
    --ink: #111111;
    --back-top: #fde7c6;
    --back-bottom: #fbae1e;
    --back-ink: #6b4708;
  }
  * { margin: 0; padding: 0; box-sizing: border-box; }
  html, body { width: 1200px; height: 900px; overflow: hidden; }
  body {
    background: linear-gradient(to bottom, var(--stage-top), var(--stage-bottom));
    font-family: "Source Sans 3", "Myriad Pro", sans-serif;
    position: relative;
  }
  .card {
    position: absolute;
    top: 306px;
    height: 271px;
    border-radius: 10px;
    overflow: hidden;
  }
  .card-front { left: 149px; width: 439px; background: var(--card-white); }
  .card-back {
    left: 608px; width: 441px;
    background: linear-gradient(to bottom, var(--back-top), var(--back-bottom));
  }

  .front-brand {
    position: absolute; left: 23px; top: 30px;
    color: var(--brand-orange); font-weight: 600;
  }
  .front-brand .brand-name { font-size: 38px; letter-spacing: 3px; line-height: 1; }
  .front-brand .brand-sub { font-size: 9px; letter-spacing: 0.6px; margin-top: 6px; }

  .contact {
    position: absolute; left: 190px; top: 118px;
    color: var(--ink); font-size: 12px; line-height: 1.3;
  }
  .contact .person-name { color: var(--brand-orange); font-size: 15px; font-weight: 600; line-height: 1.1; }
  .contact .person-role { margin-bottom: 8px; }
  .contact .label { color: var(--brand-orange); }
  .contact .ids { margin-bottom: 7px; }
  .contact .ids p { margin-bottom: 3px; }
  .contact-line { display: flex; align-items: center; gap: 6px; font-size: 11.5px; margin-bottom: 1px; }
  .contact-line svg { width: 10px; height: 10px; flex: none; fill: var(--brand-orange); }

  .back-brand {
    position: absolute; left: 0; right: 0; top: 92px;
    text-align: center; color: var(--back-ink); font-weight: 600;
  }
  .back-brand .brand-name { font-size: 62px; letter-spacing: 6px; line-height: 1; }
  .back-brand .brand-sub { font-size: 14px; letter-spacing: 1px; margin-top: 10px; }
</style>
</head>
<body>
  <section class="card card-front" aria-label="Business card front">
    <div class="front-brand">
      <div class="brand-name">TANDOR</div>
      <div class="brand-sub">ELECTRICAL &amp; COMMUNICATIONS</div>
    </div>
    <div class="contact">
      <p class="person-name">Brent Halloway</p>
      <p class="person-role">Director</p>
      <div class="ids">
        <p><span class="label">ABN:</span> 71829034618</p>
        <p><span class="label">Lic No:</span> 830472F</p>
      </div>
      <p class="contact-line">
        <svg viewBox="0 0 10 10" aria-hidden="true"><path d="M2 0.5 L3.6 0.5 L4.3 2.8 L3.2 3.7 Q4.2 5.8 6.3 6.8 L7.2 5.7 L9.5 6.4 L9.5 8 Q9.5 9.5 8 9.5 Q0.5 9 0.5 2 Q0.5 0.5 2 0.5Z"/></svg>
        0481203967
      </p>
      <p class="contact-line">
        <svg viewBox="0 0 10 10" aria-hidden="true"><rect x="0.5" y="2" width="9" height="6.5"/><path d="M0.5 2 L5 5.6 L9.5 2" stroke="#fff" stroke-width="0.9" fill="none"/></svg>
        brent@tandorelectricalandcomms.example.au
      </p>
      <p class="contact-line">
        <svg viewBox="0 0 10 10" aria-hidden="true"><circle cx="5" cy="5" r="4.5"/><path d="M0.5 5 H9.5 M5 0.5 Q2.5 5 5 9.5 M5 0.5 Q7.5 5 5 9.5" stroke="#fff" stroke-width="0.7" fill="none"/></svg>
        tandorelectricalandcomms.example.au
      </p>
    </div>
  </section>

  <section class="card card-back" aria-label="Business card back">
    <div class="back-brand">
      <div class="brand-name">TANDOR</div>
      <div class="brand-sub">ELECTRICAL &amp; COMMUNICATIONS</div>
    </div>
  </section>
</body>
</html>
```